Furniture restoration to chairs. Hand weaving.

Industry/Entity Type

Furniture

Contact Information for Business Card

The Reed Loom
Cane, rush, splint and shaker tape.
58 Tolan Rd
Fenwick Cove
ME 04583
207 - 512 - 3087
Cell: 207 - 834 - 2719

For graphics I want a picture of a caned rocking chair or maybe a rush and a cane chair.

```html
<!DOCTYPE html>
<html lang="en">
<head>
<meta charset="utf-8">
<title>The Reed Loom — Business Card</title>
<link rel="stylesheet" href="https://fonts.googleapis.com/css2?family=Source+Sans+3:wght@400;700&display=swap">
<style>
  :root {
    --backdrop: #e9e7e4;
    --card-brown: #7b4a2d;
    --card-white: #ffffff;
    --panel-tint: #f1f1f2;
    --roof-stripe: #978a84;
    --ink: #111111;
    --chair-light: #a0684a;
    --chair-dark: #6e3f25;
  }
  html, body {
    margin: 0;
    padding: 0;
    width: 1200px;
    height: 800px;
    overflow: hidden;
    background: var(--backdrop);
  }
  .canvas {
    position: relative;
    width: 1200px;
    height: 800px;
    display: flex;
    align-items: center;
    justify-content: center;
  }
  .business-card {
    position: relative;
    width: 1050px;
    height: 600px;
    background: var(--card-brown);
    overflow: hidden;
    box-shadow: 0 6px 24px rgba(0,0,0,0.18);
    font-family: "Source Sans 3", "Myriad Pro", Arial, sans-serif;
    color: var(--ink);
  }
  .roof-panel {
    position: absolute;
    inset: 0;
    width: 100%;
    height: 100%;
  }
  .chair-photo {
    position: absolute;
    left: 650px;
    top: 130px;
    width: 260px;
    height: 390px;
    background: linear-gradient(160deg, var(--chair-light), var(--chair-dark));
    opacity: 0.9;
  }
  .contact-block {
    position: absolute;
    left: 62px;
    top: 352px;
  }
  .business-name {
    margin: 0;
    font-size: 50px;
    font-weight: 700;
    letter-spacing: -0.5px;
    line-height: 1;
  }
  .tagline {
    margin: 8px 0 24px 4px;
    font-size: 19px;
    font-weight: 400;
  }
  .contact-line {
    margin: 0 0 8px 14px;
    font-size: 28px;
    font-weight: 400;
    line-height: 1.15;
  }
</style>
</head>
<body>
  <main class="canvas">
    <section class="business-card">
      <svg class="roof-panel" viewBox="0 0 1050 600" aria-hidden="true">
        <polygon points="0,300 725,58 1050,320 1050,600 0,600" fill="var(--card-white)"/>
        <polygon points="0,322 725,80 1050,340 1050,600 0,600" fill="var(--panel-tint)"/>
        <polyline points="0,322 725,80 1050,340" fill="none" stroke="var(--roof-stripe)" stroke-width="10"/>
      </svg>

      <div class="chair-photo" role="img" aria-label="Photograph of a wooden ladder-back chair with a woven rush seat"></div>

      <div class="contact-block">
        <h1 class="business-name">The Reed Loom</h1>
        <p class="tagline">Cane, rush, splint and shaker tape.</p>
        <p class="contact-line">58 Tolan Rd Fenwick Cove ME 04583</p>
        <p class="contact-line">207 - 512 - 3087</p>
        <p class="contact-line">Cell: 207 - 834 - 2719</p>
      </div>
    </section>
  </main>
</body>
</html>
```